Wordpress web design

We need a website buil in using Wordpress with 5 pages.

Pages: HOME SERVICES GALLERY TESTIMONIALS CONTACT US ABOUT US.

We are looking for a unique, professional and clean web for our construction company.

Company name: TALL OAK BUILDING SERVICES. We can olso provide you with the logo. Please don't use any flashin, intro, or any ready templates.

All your ideas are welcome.

Many thanks,
Dorian

Target Market(s)

Construction

Industry/Entity Type

Construction

Font styles to use
Sans Serif
Decorative

Requirements
Must have
• Connect with construction and London
Nice to have
• Nice and clean

```html
<!DOCTYPE html>
<html lang="en">
<head>
<meta charset="utf-8">
<title>Tall Oak Building Services – Gallery</title>
<link href="https://fonts.googleapis.com/css2?family=Didact+Gothic&family=Kreon:wght@400;700&display=swap" rel="stylesheet">
<style>
:root{
  --wood:#e6ddd5;
  --wood-dark:#d8cdc3;
  --green:#1e7a06;
  --green-deep:#175d05;
  --green-dark:#113f06;
  --green-glow:#2f8e12;
  --white:#ffffff;
  --ink:#333333;
  --muted:#555555;
  --line:#d6d6d6;
  --crumb:#efefef;
  --cream:#f4f0d8;
  --lime:#e6e27a;
  --cal-red:#c21a1a;
}
*{margin:0;padding:0;box-sizing:border-box}
html,body{width:1200px;height:1062px;overflow:hidden}
body{
  background:repeating-linear-gradient(90deg,var(--wood) 0 52px,var(--wood-dark) 52px 54px,#ebe3dc 54px 106px,var(--wood-dark) 106px 108px);
  font-family:"Kreon",serif;color:var(--ink);position:relative;
}
.page{position:absolute;left:182px;top:17px;width:834px;height:942px;background:var(--white);box-shadow:0 0 8px rgba(0,0,0,.25)}
.topbar{position:absolute;left:0;top:0;width:100%;height:30px;background:var(--green)}
.topbar .notch{position:absolute;left:388px;top:30px;width:0;height:0;border-left:7px solid transparent;border-right:7px solid transparent;border-top:9px solid var(--green)}
.social{position:absolute;left:13px;top:8px;display:flex;gap:7px}
.social span{width:14px;height:14px;border-radius:50%;background:#dfe9d6;opacity:.85}
.logo{position:absolute;left:49px;top:58px;font-family:"Didact Gothic",sans-serif;font-size:41px;letter-spacing:2px;color:#111}
.call{position:absolute;left:583px;top:57px;display:flex;align-items:center;gap:12px;font-size:16px;font-weight:700;color:#333}
.nav{position:absolute;left:17px;top:135px;width:800px;height:34px;border-top:1px dotted #bbb;border-bottom:1px dotted #bbb;display:flex;align-items:center;font-size:13.5px;color:#333}
.nav a{color:inherit;text-decoration:none;padding:0 17px;border-right:1px solid var(--line);line-height:18px}
.nav a:last-child{border-right:0}
.nav a.active{background:var(--green);color:var(--white);font-weight:700;line-height:28px;padding:0 17px;margin:0 6px;border:0}
.crumb{position:absolute;left:17px;top:204px;width:800px;height:36px;background:var(--crumb);border:1px solid #ccc;font-size:17px;line-height:34px;padding-left:10px;color:#333}
.gallery{position:absolute;left:61px;top:281px;display:grid;grid-template-columns:repeat(3,152px);grid-auto-rows:76px;column-gap:6px;row-gap:6.5px}
.gallery div{width:152px;height:76px}
.calendar{position:absolute;left:613px;top:253px;width:197px;font-size:11px;color:#777}
.calendar .title{text-align:center;font-size:9px;letter-spacing:1px;color:#333;margin-bottom:9px}
.calendar table{width:100%;border-collapse:collapse}
.calendar td,.calendar th{border:1px solid var(--line);height:22px;text-align:center;font-weight:400}
.calendar th{background:#dcdcdc;color:#fff;height:22px}
.calendar .today{color:var(--cal-red);font-weight:700}
.calendar .pad{border:1px solid var(--line)}
.footer{position:absolute;left:0;top:724px;width:100%;height:182px;background:radial-gradient(ellipse 260px 200px at 330px 70px,var(--green-glow),var(--green) 55%,var(--green-deep) 100%)}
.fcol{position:absolute;top:25px;width:190px}
.fcol h3{font-size:18px;font-weight:700;color:var(--cream);padding-bottom:8px;border-bottom:1px solid #4c8a2a;margin-bottom:14px}
.fcol p{font-size:12px;line-height:19px;color:var(--lime);width:185px}
.fcol ul{list-style:none;font-size:12px;line-height:19px;color:var(--lime)}
.fcol li:before{content:"•";color:#fff;margin-right:8px}
.search{position:absolute;left:632px;top:22px;width:155px;height:24px;background:var(--green-dark);display:flex;align-items:center;font-size:12px;color:var(--lime);padding-left:7px}
.search .btn{position:absolute;right:0;top:0;width:28px;height:24px;background:#1c4a0c;display:flex;align-items:center;justify-content:center}
.bottombar{position:absolute;left:0;top:906px;width:100%;height:36px;background:var(--green-dark);font-size:11px;color:#a6c56e;line-height:36px;padding-left:17px}
.bottombar .up{position:absolute;right:16px;top:10px}
</style>
</head>
<body>
<div class="page">
  <header>
    <div class="topbar">
      <div class="social"><span></span><span></span><span></span><span></span></div>
      <div class="notch"></div>
    </div>
    <div class="logo">Your logo</div>
    <div class="call">
      <svg width="14" height="24" viewBox="0 0 14 24"><rect x="1" y="1" width="12" height="22" rx="2" fill="none" stroke="#999" stroke-width="2"/><rect x="4" y="4" width="6" height="13" fill="#bbb"/></svg>
      <span>Call 24 Hours: 1.800.555.0199</span>
    </div>
    <nav class="nav">
      <a href="#">Home</a><a href="#">SERVICES</a><a href="#" class="active">GALLERY</a><a href="#">TESTIMONIALS</a><a href="#">CONTACT US</a><a href="#">ABOUT US</a>
    </nav>
  </header>

  <div class="crumb">Gallery &nbsp;»</div>

  <section class="gallery">
    <div role="img" aria-label="Sunny park with trees" style="background:linear-gradient(180deg,#6b8fb3,#4f7a3a 60%,#2f4a22)"></div>
    <div role="img" aria-label="Wooden room interior" style="background:linear-gradient(135deg,#5a3d2e,#8a6a55,#3a2a22)"></div>
    <div role="img" aria-label="Poster artwork in gold tones" style="background:linear-gradient(135deg,#3a2a10,#c99b2a,#5a1a10)"></div>
    <div role="img" aria-label="Dark grey graphic" style="background:linear-gradient(180deg,#3e3e3e,#2a2a2a)"></div>
    <div role="img" aria-label="Portrait in red tones" style="background:linear-gradient(135deg,#e8d2c8,#a82a2a,#3a1a1a)"></div>
    <div role="img" aria-label="Close-up hand photo" style="background:linear-gradient(135deg,#2a3a2a,#7a8a6a,#1e2a1e)"></div>
    <div role="img" aria-label="Blue sky with clouds" style="background:linear-gradient(160deg,#1d4c9a,#6fa1d8,#dfe9f5)"></div>
    <div role="img" aria-label="Butterfly on a branch" style="background:linear-gradient(135deg,#5a6e6a,#2e3a36,#8a9a8a)"></div>
    <div role="img" aria-label="Bird on a green branch" style="background:linear-gradient(135deg,#b9d25a,#7aa22e,#3a5a1a)"></div>
    <div role="img" aria-label="City street with tram" style="background:linear-gradient(180deg,#a8b0bc,#8a7a70 60%,#5a5e66)"></div>
    <div role="img" aria-label="Misty forest path" style="background:linear-gradient(180deg,#6a7658,#4a5640,#2e3426)"></div>
    <div role="img" aria-label="Classic living room interior" style="background:linear-gradient(135deg,#2a1a10,#7a4a26,#1e140e)"></div>
    <div role="img" aria-label="City street with tram" style="background:linear-gradient(180deg,#a8b0bc,#8a7a70 60%,#5a5e66)"></div>
    <div role="img" aria-label="Misty forest path" style="background:linear-gradient(180deg,#6a7658,#4a5640,#2e3426)"></div>
    <div role="img" aria-label="Classic living room interior" style="background:linear-gradient(135deg,#2a1a10,#7a4a26,#1e140e)"></div>
  </section>

  <aside class="calendar">
    <div class="title">MARCH 2015</div>
    <table>
      <tr><th>M</th><th>T</th><th>W</th><th>T</th><th>F</th><th>S</th><th>S</th></tr>
      <tr><td></td><td></td><td></td><td></td><td></td><td></td><td>1</td></tr>
      <tr><td>2</td><td>3</td><td>4</td><td>5</td><td>6</td><td>7</td><td>8</td></tr>
      <tr><td>9</td><td>10</td><td>11</td><td>12</td><td>13</td><td class="today">14</td><td>15</td></tr>
      <tr><td>16</td><td>17</td><td>18</td><td>19</td><td>20</td><td>21</td><td>22</td></tr>
      <tr><td>23</td><td>24</td><td>25</td><td>26</td><td>27</td><td>28</td><td>29</td></tr>
      <tr><td>30</td><td>31</td><td colspan="5"></td></tr>
      <tr><td colspan="3"></td><td></td><td colspan="3"></td></tr>
    </table>
  </aside>

  <footer class="footer">
    <div class="fcol" style="left:17px">
      <h3>Adout Company</h3>
      <p>We are construction partners who are passionate about what we do and our partners' success.</p>
    </div>
    <div class="fcol" style="left:226px">
      <h3>Archives Widget</h3>
      <ul><li>January 2010</li><li>December 2009</li><li>November 2009</li><li>October 2009</li></ul>
    </div>
    <div class="fcol" style="left:430px">
      <h3>Categories</h3>
      <ul><li>Entertainment</li><li>Technology</li><li>Template Design</li><li>Sports &amp; Recreation</li><li>Jobs &amp; Lifestyle</li></ul>
    </div>
    <div class="search">Search
      <span class="btn"><svg width="12" height="12" viewBox="0 0 12 12"><circle cx="5" cy="5" r="3.5" fill="none" stroke="#fff" stroke-width="1.6"/><line x1="7.5" y1="7.5" x2="11" y2="11" stroke="#fff" stroke-width="1.8"/></svg></span>
    </div>
  </footer>
  <div class="bottombar">Copyright © 2015 TALL OAK BUILDING SERVICES.
    <svg class="up" width="16" height="16" viewBox="0 0 16 16"><path d="M3 14 L11 5 M6 4 H12 V10" fill="none" stroke="#fff" stroke-width="2.4"/></svg>
  </div>
</div>
</body>
</html>
```